We have developed a fully functional App called Corvalink. However, it requires a nicer GUI. You can see screenshots of our App on www.corvalink-example.com under "Tutorial". For those of you with Android, you can also install it. When you go to Corvalink-example.com, your phone will automatically redirect you to download. From there, you'll get a better idea of what our App looks like and how your design can make it way better. Please note we expect a design idea for most screens (there's about 8 screens) but do just one screen first and if you win, you can do the other 8 after.

Target Market(s)

People looking for dating / flirting

Industry/Entity Type

Android

Requirements
Must have
• sleek looking

```html
<!DOCTYPE html>
<html lang="en">
<head>
<meta charset="utf-8">
<title>Corvalink – Chat</title>
<link href="https://fonts.googleapis.com/css2?family=Roboto:wght@300;400;500&display=swap" rel="stylesheet">
<style>
  :root{
    --canvas:#e6e8ec;
    --screen:#1d222c;
    --bar:#171b23;
    --bubble:#2a303c;
    --bubble-own:#262c37;
    --name-blue:#5aaedc;
    --name-green:#7cc36a;
    --text:#a9b0bc;
    --icon:#7d8594;
    --accent:#e2393f;
    --avatar-a:#c98a5e;
    --avatar-b:#8aa35c;
  }
  *{box-sizing:border-box;margin:0;padding:0}
  html,body{width:1200px;height:900px;overflow:hidden}
  body{background:var(--canvas);font-family:"Roboto",sans-serif;display:flex;align-items:center;justify-content:center}

  .app-screen{width:440px;height:800px;background:var(--screen);display:flex;flex-direction:column;overflow:hidden;box-shadow:0 20px 50px rgba(0,0,0,.25)}

  .top-bar{height:64px;background:var(--bar);display:flex;align-items:center;padding:0 20px;gap:16px}
  .top-bar .brand{flex:1;display:flex;align-items:center;gap:8px;color:#e8ebf0;font-size:20px;font-weight:400;letter-spacing:.5px}
  .brand-dot{width:10px;height:10px;border-radius:50%;background:var(--accent)}
  .top-bar svg{width:24px;height:24px;stroke:var(--icon);fill:none;stroke-width:2;stroke-linecap:round}

  .chat-thread{flex:1;padding:26px 20px 0;display:flex;flex-direction:column;gap:26px;overflow:hidden}
  .message{display:flex;align-items:flex-start;gap:14px}
  .message.own{flex-direction:row-reverse}
  .avatar{width:46px;height:46px;border-radius:50%;flex:none;border:2px solid #39404d}
  .avatar.anna{background:radial-gradient(circle at 40% 40%,#e0a67a,var(--avatar-a) 60%,#7a4f36)}
  .avatar.mark{background:radial-gradient(circle at 40% 40%,#b4c97d,var(--avatar-b) 60%,#4f6436)}
  .bubble{background:var(--bubble);border-radius:6px;padding:12px 16px;max-width:250px;position:relative}
  .message.own .bubble{background:var(--bubble-own)}
  .bubble::before{content:"";position:absolute;top:16px;left:-7px;border:7px solid transparent;border-left:0;border-right-color:var(--bubble)}
  .message.own .bubble::before{left:auto;right:-7px;border-right:0;border-left:7px solid var(--bubble-own)}
  .sender{font-size:13px;font-weight:500;margin-bottom:5px}
  .anna-name{color:var(--name-blue)}
  .mark-name{color:var(--name-green)}
  .text{font-size:13px;font-weight:300;line-height:1.5;color:var(--text)}

  .bottom-bar{height:76px;background:var(--bar);display:flex;align-items:center;justify-content:space-between;padding:0 40px}
  .bottom-bar svg{width:26px;height:26px;stroke:var(--icon);fill:none;stroke-width:2;stroke-linecap:round}
  .record-button{width:44px;height:44px;border-radius:50%;background:var(--accent);box-shadow:0 0 0 6px #2a303c}
</style>
</head>
<body>
<main class="app-screen">
  <header class="top-bar">
    <svg viewBox="0 0 24 24" aria-label="Menu"><path d="M4 6h16M4 12h16M4 18h16"/></svg>
    <div class="brand"><span class="brand-dot"></span>Corvalink</div>
    <svg viewBox="0 0 24 24" aria-label="Settings"><circle cx="12" cy="12" r="3"/><circle cx="12" cy="12" r="8"/></svg>
  </header>

  <section class="chat-thread">
    <article class="message">
      <div class="avatar anna" role="img" aria-label="Profile photo of Anna"></div>
      <div class="bubble"><p class="sender anna-name">Anna</p><p class="text">Hey there! Loved your profile photo.</p></div>
    </article>
    <article class="message own">
      <div class="avatar mark" role="img" aria-label="Profile photo of Mark"></div>
      <div class="bubble"><p class="sender mark-name">Mark</p><p class="text">Thanks! Coffee this weekend?</p></div>
    </article>
    <article class="message">
      <div class="avatar anna" role="img" aria-label="Profile photo of Anna"></div>
      <div class="bubble"><p class="sender anna-name">Anna</p><p class="text">Sounds great. Saturday morning works for me, any good place?</p></div>
    </article>
    <article class="message own">
      <div class="avatar mark" role="img" aria-label="Profile photo of Mark"></div>
      <div class="bubble"><p class="sender mark-name">Mark</p><p class="text">I know a cozy spot downtown.</p></div>
    </article>
    <article class="message">
      <div class="avatar anna" role="img" aria-label="Profile photo of Anna"></div>
      <div class="bubble"><p class="sender anna-name">Anna</p><p class="text">Perfect, see you there!</p></div>
    </article>
  </section>

  <footer class="bottom-bar">
    <svg viewBox="0 0 24 24" aria-label="Back"><path d="M15 5l-7 7 7 7"/></svg>
    <div class="record-button" aria-label="Record"></div>
    <svg viewBox="0 0 24 24" aria-label="Send"><path d="M4 12h15M13 6l6 6-6 6"/></svg>
  </footer>
</main>
</body>
</html>
```